Clean and modern business cards

Looking for an updated business card design for my dental office “corvanta dental” . Looking for a modern clean / sleek design . I’m thinking black background but open to seeing other options . One side needs to have an appointment card . Card needs to have logo, dentist name , phone, email , address . I’ve attached couple of cards I thought were cool as well as my logo
Target Market(s)
Dental patients
Industry/Entity Type
Dentistry
Contact Information for Business Card
Phone email address

```html
<!DOCTYPE html>
<html lang="en">
<head>
<meta charset="utf-8">
<title>Corvanta Dental – Business Card</title>
<link rel="stylesheet" href="https://fonts.googleapis.com/css2?family=Open+Sans:wght@400;600;700&family=Didact+Gothic&family=Fjalla+One&display=swap">
<style>
  :root {
    --stage-light: #ffffff;
    --stage-dark: #1c1c1c;
    --card-black: #050507;
    --card-white: #ffffff;
    --accent-yellow: #ffd400;
    --accent-teal: #0e9bbd;
    --accent-green: #9bc21d;
    --accent-red: #e30e16;
    --ink: #111111;
    --rule: #555555;
    --mark-tint: #e6e3ef;
  }
  * { margin: 0; padding: 0; box-sizing: border-box; }
  html, body { width: 1200px; height: 1000px; overflow: hidden; }
  body { position: relative; font-family: "Open Sans", Arial, sans-serif; }

  .stage { position: absolute; left: 0; width: 1200px; height: 500px; }
  .stage--front { top: 0; background: var(--stage-light); }
  .stage--back { top: 500px; background: var(--stage-dark); }

  .card { position: absolute; left: 321px; width: 564px; height: 323px; overflow: hidden; }

  /* Front */
  .card--front { top: 84px; background: var(--card-black); color: #fff; }
  .brand { position: absolute; display: flex; align-items: center; }
  .brand__dot { border-radius: 50%; flex: none; }
  .brand__name { font-family: "Open Sans", Arial, sans-serif; font-weight: 700; letter-spacing: 1px; white-space: nowrap; }
  .card--front .brand { left: 134px; top: 96px; }
  .card--front .brand__dot { width: 86px; height: 86px; background: var(--accent-teal); margin-right: 16px; }
  .card--front .brand__name { font-size: 27px; color: #fff; }

  .dentist-name {
    position: absolute; left: 164px; top: 209px; width: 236px; height: 26px;
    background: var(--accent-yellow); color: var(--ink);
    font-size: 17px; font-weight: 600; text-align: center; line-height: 26px;
  }
  .contact { position: absolute; left: 0; width: 100%; text-align: center; font-size: 12.5px; line-height: 17px; }
  .contact--address { top: 237px; }
  .contact--web { top: 254px; }
  .contact .sep { color: var(--accent-yellow); padding: 0 2px; }

  /* Back */
  .card--back { top: 92px; background: var(--card-white); color: var(--ink); }
  .card--back .brand { left: 36px; top: 32px; }
  .card--back .brand__dot { width: 44px; height: 44px; background: var(--accent-teal); margin-right: 10px; }
  .card--back .brand__name { font-size: 16px; color: var(--ink); }

  .faint-mark { position: absolute; left: 350px; top: 130px; width: 240px; height: 240px; border-radius: 50%; background: var(--mark-tint); opacity: .55; }

  .band { position: absolute; left: 0; width: 100%; display: flex; }
  .band__tab { width: 20px; flex: none; }
  .band__body { flex: 1; }
  .band--heading { top: 94px; height: 29px; }
  .band--heading .band__tab { background: var(--accent-teal); }
  .band--heading .band__body { background: #000; color: #fff; font-family: "Didact Gothic", sans-serif; font-size: 22px; line-height: 29px; padding-left: 16px; }
  .band--notice { top: 204px; height: 52px; }
  .band--notice .band__tab { background: var(--accent-green); }
  .band--notice .band__body { background: var(--accent-red); color: #fff; font-family: "Fjalla One", sans-serif; font-size: 13.5px; line-height: 19px; text-align: center; padding-top: 7px; text-transform: uppercase; }

  .field { position: absolute; display: flex; align-items: flex-end; font-family: "Didact Gothic", sans-serif; }
  .field__label { font-size: 22px; line-height: 24px; }
  .field__line { border-bottom: 1px solid var(--rule); margin-left: 12px; margin-bottom: 3px; }
  .field--date { left: 69px; top: 133px; }
  .field--time { left: 69px; top: 166px; }
  .field--date .field__line, .field--time .field__line { width: 177px; margin-left: 16px; }
  .field--date .field__line { margin-left: 18px; }
  .field--note { left: 36px; top: 270px; }
  .field--note .field__label { font-size: 17px; }
  .field--note .field__line { width: 436px; margin-left: 10px; }
</style>
</head>
<body>
  <section class="stage stage--front">
    <article class="card card--front">
      <div class="brand">
        <span class="brand__dot"></span>
        <span class="brand__name">CORVANTA DENTAL</span>
      </div>
      <p class="dentist-name">DR. ELIAS VANTOR</p>
      <p class="contact contact--address">2480 LARKFIELD WAY, WINNIPEG, MB <span class="sep">|</span> (204) 555 0172</p>
      <p class="contact contact--web">WWW.CORVANTAWPG.CA <span class="sep">|</span> CONTACT@CORVANTAWPG.CA</p>
    </article>
  </section>

  <section class="stage stage--back">
    <article class="card card--back">
      <span class="faint-mark" aria-hidden="true"></span>
      <div class="brand">
        <span class="brand__dot"></span>
        <span class="brand__name">CORVANTA DENTAL</span>
      </div>
      <div class="band band--heading">
        <span class="band__tab"></span>
        <h2 class="band__body" style="font-weight:400">Your Next Appointment is :</h2>
      </div>
      <div class="field field--date"><span class="field__label">Date</span><span class="field__line"></span></div>
      <div class="field field--time"><span class="field__label">Time</span><span class="field__line"></span></div>
      <div class="band band--notice">
        <span class="band__tab"></span>
        <p class="band__body">To cancel or reschedule please notify us at least 48hrs<br>prior to your scheduled appointment.</p>
      </div>
      <div class="field field--note"><span class="field__label">Note :</span><span class="field__line"></span></div>
    </article>
  </section>
</body>
</html>
```